Trade show booth design

I have most of what I'm wanting the back display and front stand to look like but I need someone to slightly modify the design, put it proper sizing and at least 72 dpi. I'm including a few pics of what I'm thinking for the back and front displays, as well as our logo. The link to the actual booth is here: https://trovenk.us/products/10x10-booth-backlit-display-kit-01

```html
<!DOCTYPE html>
<html lang="en">
<head>
<meta charset="utf-8">
<title>Briskwell – Trade Show Back Wall</title>
<link rel="stylesheet" href="https://fonts.googleapis.com/css2?family=Oswald:wght@400;600&family=Roboto:wght@400&display=swap">
<style>
  :root {
    --page-bg: #e4e4e4;
    --brand-blue: #0b5a8e;
    --brand-orange: #e64a1f;
    --white: #ffffff;
    --photo-sky: #c9d7e2;
    --photo-trees: #8a8c3e;
    --photo-roof: #d8dbe0;
    --photo-lot: #5f6166;
  }
  html, body {
    margin: 0;
    padding: 0;
    width: 1200px;
    height: 2308px;
    overflow: hidden;
    background: var(--page-bg);
  }
  .banner {
    position: absolute;
    left: 100px;
    top: 654px;
    width: 1000px;
    height: 1000px;
    background: var(--brand-blue);
    overflow: hidden;
    color: var(--white);
  }
  .banner-graphics {
    position: absolute;
    inset: 0;
  }
  .brand-name {
    position: absolute;
    left: 79px;
    top: 72px;
    margin: 0;
    font-family: "Oswald", sans-serif;
    font-weight: 600;
    font-size: 72px;
    line-height: 1;
    letter-spacing: 2px;
    text-transform: uppercase;
    color: var(--white);
  }
  .headline {
    position: absolute;
    left: 58px;
    top: 270px;
    margin: 0;
    font-family: "Oswald", sans-serif;
    font-weight: 600;
    font-size: 58px;
    line-height: 54px;
    text-transform: uppercase;
    transform: scaleX(0.74);
    transform-origin: left top;
    white-space: nowrap;
  }
  .accent-rule {
    position: absolute;
    left: 58px;
    width: 95px;
    height: 8px;
    background: linear-gradient(to right, var(--white) 0 60%, var(--brand-orange) 60% 100%);
  }
  .accent-rule--headline { top: 455px; }
  .accent-rule--contact { top: 873px; }
  .benefit-list {
    position: absolute;
    left: 58px;
    top: 498px;
    margin: 0;
    padding: 0;
    list-style: none;
  }
  .benefit {
    display: flex;
    align-items: center;
    height: 60px;
    margin-bottom: 12px;
  }
  .benefit-icon {
    width: 54px;
    height: 60px;
    flex: none;
  }
  .benefit-text {
    margin-left: 18px;
    font-family: "Oswald", sans-serif;
    font-weight: 400;
    font-size: 25px;
    line-height: 25px;
    text-transform: uppercase;
    white-space: nowrap;
  }
  .call-line {
    position: absolute;
    left: 58px;
    top: 744px;
    margin: 0;
    font-family: "Oswald", sans-serif;
    font-weight: 600;
    font-size: 72px;
    line-height: 1;
    transform: scaleX(0.76);
    transform-origin: left top;
    white-space: nowrap;
  }
  .web-address {
    position: absolute;
    left: 58px;
    top: 820px;
    margin: 0;
    font-family: "Roboto", sans-serif;
    font-weight: 400;
    font-size: 34px;
    line-height: 1;
    letter-spacing: 0.5px;
    white-space: nowrap;
  }
</style>
</head>
<body>
  <section class="banner">
    <svg class="banner-graphics" viewBox="0 0 1000 1000" width="1000" height="1000">
      <defs>
        <linearGradient id="aerial-tones" x1="0" y1="0" x2="0" y2="1">
          <stop offset="0" stop-color="var(--photo-sky)"/>
          <stop offset="0.25" stop-color="var(--photo-trees)"/>
          <stop offset="0.5" stop-color="var(--photo-roof)"/>
          <stop offset="0.8" stop-color="var(--photo-lot)"/>
          <stop offset="1" stop-color="#4c6a3a"/>
        </linearGradient>
      </defs>
      <polygon class="hex-accent-orange" fill="var(--brand-orange)" points="820,65 889,105 889,185 820,225 751,185 751,105"/>
      <polygon class="hex-accent-white" fill="var(--white)" points="885,209 908,222 908,248 885,261 862,248 862,222"/>
      <polygon class="hex-backing-orange" fill="var(--brand-orange)" points="700,353 897,467 897,694 700,807 503,694 503,467"/>
      <polygon class="hex-backing-white" fill="var(--white)" points="751,289 963,412 963,656 751,779 539,656 539,412"/>
      <polygon class="hex-frame" fill="var(--brand-blue)" stroke="var(--white)" stroke-width="1.5" points="700,184 938,322 938,597 700,734 462,597 462,322"/>
      <polygon class="hex-photo" role="img" aria-label="Aerial photo of a large commercial building with a white roof, parking lot and autumn trees" fill="url(#aerial-tones)" points="700,207 919,334 919,586 700,713 481,586 481,334"/>
      <polygon class="hex-accent-white" fill="var(--white)" points="620,780 681,815 681,885 620,920 559,885 559,815"/>
    </svg>

    <h1 class="brand-name">Briskwell</h1>

    <h2 class="headline">Revolutionizing<br>the commercial<br>roofing industry</h2>
    <div class="accent-rule accent-rule--headline"></div>

    <ul class="benefit-list">
      <li class="benefit">
        <svg class="benefit-icon" viewBox="0 0 54 60" aria-hidden="true">
          <polygon points="27,2 52,16 52,44 27,58 2,44 2,16" fill="var(--white)"/>
          <circle cx="27" cy="23" r="5" fill="var(--brand-orange)"/>
          <circle cx="17" cy="27" r="4" fill="var(--brand-orange)"/>
          <circle cx="37" cy="27" r="4" fill="var(--brand-orange)"/>
          <path d="M19 44 v-8 a8 8 0 0 1 16 0 v8 z M10 42 v-6 a6 6 0 0 1 9 -5 M44 42 v-6 a6 6 0 0 0 -9 -5" fill="var(--brand-orange)"/>
        </svg>
        <span class="benefit-text">Data-driven roof asset<br>management platform</span>
      </li>
      <li class="benefit">
        <svg class="benefit-icon" viewBox="0 0 54 60" aria-hidden="true">
          <polygon points="27,2 52,16 52,44 27,58 2,44 2,16" fill="var(--white)"/>
          <rect x="14" y="36" width="5" height="8" fill="var(--brand-orange)"/>
          <rect x="22" y="32" width="5" height="12" fill="var(--brand-orange)"/>
          <rect x="30" y="27" width="5" height="17" fill="var(--brand-orange)"/>
          <rect x="38" y="22" width="5" height="22" fill="var(--brand-orange)"/>
          <path d="M13 30 L24 22 L30 25 L40 15" stroke="var(--brand-orange)" stroke-width="2.5" fill="none"/>
          <path d="M36 14 L42 13 L41 19 z" fill="var(--brand-orange)"/>
        </svg>
        <span class="benefit-text">Improve performance.<br>Reduce spend.</span>
      </li>
      <li class="benefit">
        <svg class="benefit-icon" viewBox="0 0 54 60" aria-hidden="true">
          <polygon points="27,2 52,16 52,44 27,58 2,44 2,16" fill="var(--white)"/>
          <circle cx="27" cy="27" r="12" fill="none" stroke="var(--brand-orange)" stroke-width="4"/>
          <path d="M21 27 L26 32 L34 22" stroke="var(--brand-orange)" stroke-width="3.5" fill="none"/>
          <path d="M20 37 L17 47 L22 45 L25 49 L27 40 M34 37 L37 47 L32 45 L29 49 L27 40" fill="var(--brand-orange)"/>
        </svg>
        <span class="benefit-text">Connecting national accounts<br>with best-in-class roofing</span>
      </li>
    </ul>

    <p class="call-line">CALL 800-555-0142</p>
    <p class="web-address">www.briskwell-roofs.com</p>
    <div class="accent-rule accent-rule--contact"></div>
  </section>
</body>
</html>
```